Custom Cabinet Shop Needs a website design

Hi,
We need a website for a Custom Cabinet Shop and Cabinet parts manufacturing business.
The business has two sides to it. One side provides custom Kitchens, vanities, entertainment units, offices and what not to homeowners and contractors.
The 2nd side of the business provides built to order cabinet boxes and other parts required to put together a project to other cabinet shops, small contractors looking to install there own cabinets.
Website will need a Gallery to display work.
Color scheme to go well with logo.
current website is www.brindlemoorcustomcabinets.com
being changed to www.brindlemoor.ca
Tagline "Joinery with Spirit"
Mission Statement "Our passion is to deliver inspired cabinetry solutions to suit all your needs, supported by our phenomenal star class customer service"
The website should convey quality and professionalism.
Thank you.
Target Market(s)
Homeowners/ Contractors
Industry/Entity Type
Entertainment
Coding
Coded - Design and coding required
Number of Pages Required
1 page
Look and feel
Each slider illustrates characteristics of the customer's brand and the style your logo design should communicate.

```html
<!DOCTYPE html>
<html lang="en">
<head>
<meta charset="utf-8">
<title>Brindlemoor Custom Cabinets</title>
<link href="https://fonts.googleapis.com/css2?family=Lato:wght@300;400;700;900&display=swap" rel="stylesheet">
<style>
:root{
  --accent:#f2672a;
  --accent-soft:#f59a6e;
  --ink:#1b1b1b;
  --text:#555;
  --muted:#888;
  --band:#f1f1f1;
  --white:#fff;
  --field:#f3f3f3;
  --rule:#dcdcdc;
  --footer:#0c0c0c;
}
*{margin:0;padding:0;box-sizing:border-box}
html,body{width:1200px;height:3209px;overflow:hidden}
body{position:relative;background:var(--white);font-family:'Lato',sans-serif;color:var(--text)}
.section{position:absolute;left:0;width:1200px}
.title{position:absolute;left:0;width:1200px;text-align:center;font-weight:900;font-size:24px;letter-spacing:2px;color:var(--ink)}
.title::after{content:"";display:block;width:86px;height:5px;margin:11px auto 0;background:linear-gradient(90deg,#2a1a12,var(--accent),#2a1a12);border-radius:2px}

/* nav */
.nav{top:0;height:82px;background:var(--white)}
.nav a{position:absolute;top:35px;font-size:10px;letter-spacing:1px;color:#333;text-decoration:none;text-transform:uppercase}
.nav .sep{position:absolute;top:24px;width:1px;height:34px;background:var(--rule)}
.brand{position:absolute;left:520px;top:22px;width:165px;height:40px;display:flex;align-items:center;justify-content:center;gap:7px}
.brand-mark{width:13px;height:13px;border-radius:50%;background:var(--accent)}
.brand-name{font-weight:900;font-size:15px;letter-spacing:.5px;color:var(--ink)}

/* hero */
.hero{top:82px;height:438px;background:linear-gradient(100deg,#cfd6dc 0%,#e9e8e5 18%,#6f5f55 34%,#d9d6d1 52%,#2c2c2e 70%,#efece7 86%,#d8d2c8 100%)}
.tagline{position:absolute;left:402px;top:177px;width:394px;height:81px;border:3px solid rgba(255,255,255,.9);background:rgba(255,255,255,.82);display:flex;align-items:center;justify-content:center;font-size:29px;font-weight:300;letter-spacing:1.5px;color:#333;text-transform:uppercase}
.tagline span{color:var(--accent)}

/* mission */
.mission{top:520px;height:197px}
.mission .title{top:42px}
.mission p{position:absolute;top:101px;left:0;width:1200px;text-align:center;font-size:15px;line-height:22px;letter-spacing:1px;color:var(--text)}

/* gallery */
.gallery{top:717px;height:755px;background:var(--band)}
.gallery .title{top:43px}
.tile{position:absolute}

/* services */
.services{top:1472px;height:635px}
.services .title{top:46px}
.divider{position:absolute;left:600px;top:120px;width:1px;height:490px;background:var(--rule)}
.svc{position:absolute;top:131px;width:252px}
.svc h3{text-align:center;font-weight:400;font-size:21px;letter-spacing:2px;color:var(--accent-soft);text-transform:uppercase}
.svc .photo{margin:18px 0 0;height:175px;border:6px solid #e6e6e6}
.svc p{margin-top:13px;font-size:11px;line-height:17px;letter-spacing:.6px;color:var(--text)}
.svc p + p{margin-top:15px}

/* warranty */
.warranty{top:2107px;height:684px;background:var(--band)}
.warranty .title{top:46px}
.terms{position:absolute;left:302px;top:118px;width:764px;font-size:9px;line-height:13px;letter-spacing:.4px;color:var(--text)}
.terms p{margin-bottom:12px}
.terms b{color:var(--accent)}
.terms strong{color:#333}

/* contact */
.contact{top:2791px;height:381px}
.contact .title{top:48px}
.form{position:absolute;left:314px;top:124px;width:238px}
.field{height:28px;margin-bottom:8px;background:var(--field);border:1px solid #e2e2e2;font-size:10px;color:#444;padding:7px 9px}
.field.message{height:68px}
.submit{margin-top:14px;width:75px;height:26px;background:var(--accent);color:#fff;font-size:11px;font-weight:700;display:flex;align-items:center;justify-content:center}
.details{position:absolute;left:631px;top:118px;width:260px;font-size:11px;line-height:21px;color:#333;letter-spacing:.5px}
.details h4{font-size:11px;font-weight:700}
.details hr{border:0;border-top:1px solid var(--rule);margin:8px 0}
.line{display:flex;align-items:center;gap:7px}
.dot{width:14px;height:14px;border-radius:50%;background:var(--accent);display:flex;align-items:center;justify-content:center}
.social{display:flex;gap:5px;margin-top:12px}
.social span{width:18px;height:18px;border-radius:50%;background:var(--ink)}

/* footer */
.footer{top:3172px;height:37px;background:var(--footer);color:#bbb;font-size:9px;text-align:center;line-height:37px;letter-spacing:.5px}
</style>
</head>
<body>

<header class="section nav">
  <a style="left:362px">Gallery</a>
  <span class="sep" style="left:423px"></span>
  <a style="left:443px">Services</a>
  <span class="sep" style="left:510px"></span>
  <div class="brand"><span class="brand-mark"></span><span class="brand-name">BRINDLEMOOR</span></div>
  <span class="sep" style="left:698px"></span>
  <a style="left:723px">Warranty</a>
  <span class="sep" style="left:788px"></span>
  <a style="left:806px">Contact</a>
</header>

<section class="section hero" role="img" aria-label="Bright kitchen with white shaker cabinets, dark island and patio doors">
  <div class="tagline"><span>Joinery</span>&nbsp;with Spirit</div>
</section>

<section class="section mission">
  <h2 class="title">OUR MISSION</h2>
  <p>Our passion is to deliver inspired cabinetry solutions to suit all your needs,<br>supported by our phenomenal star class customer service</p>
</section>

<section class="section gallery">
  <h2 class="title">GALLERY</h2>
  <div class="tile" role="img" aria-label="Kitchen with pendant lights" style="left:141px;top:124px;width:178px;height:135px;background:linear-gradient(160deg,#8a7565,#3a2c25)"></div>
  <div class="tile" role="img" aria-label="Dark wall unit" style="left:141px;top:264px;width:178px;height:240px;background:linear-gradient(160deg,#5b4436,#231812)"></div>
  <div class="tile" role="img" aria-label="Entertainment centre" style="left:141px;top:509px;width:178px;height:100px;background:linear-gradient(160deg,#7a3a2a,#2a1a14)"></div>

  <div class="tile" role="img" aria-label="White kitchen" style="left:325px;top:124px;width:178px;height:135px;background:linear-gradient(160deg,#d8d4ce,#8a8480)"></div>
  <div class="tile" role="img" aria-label="Built-in white shelving" style="left:325px;top:266px;width:178px;height:135px;background:linear-gradient(160deg,#7a8a92,#2e3a40)"></div>
  <div class="tile" role="img" aria-label="Kitchen with dark cabinets" style="left:325px;top:405px;width:178px;height:120px;background:linear-gradient(160deg,#8a6240,#2a1b12)"></div>
  <div class="tile" role="img" aria-label="Bar with wine rack" style="left:325px;top:529px;width:178px;height:156px;background:linear-gradient(160deg,#6a5040,#1e1510)"></div>

  <div class="tile" role="img" aria-label="Kitchen island and hardwood floor" style="left:509px;top:124px;width:178px;height:240px;background:linear-gradient(170deg,#e6e2dc,#8b6a4c)"></div>
  <div class="tile" role="img" aria-label="Bathroom vanity with tub" style="left:509px;top:370px;width:178px;height:276px;background:linear-gradient(170deg,#b8a48e,#3e2e26)"></div>

  <div class="tile" role="img" aria-label="Glass-door display cabinet" style="left:693px;top:128px;width:180px;height:131px;background:linear-gradient(160deg,#d0cbc4,#3a2a22)"></div>
  <div class="tile" role="img" aria-label="Kitchen with island" style="left:693px;top:266px;width:180px;height:135px;background:linear-gradient(160deg,#c7b7a4,#3e2e24)"></div>
  <div class="tile" role="img" aria-label="Kitchen with stone counter" style="left:693px;top:405px;width:180px;height:280px;background:linear-gradient(170deg,#4a3a33,#a58d6c 60%,#5a3a24)"></div>

  <div class="tile" role="img" aria-label="Tall dark cabinet" style="left:879px;top:124px;width:180px;height:240px;background:linear-gradient(170deg,#f4f2ef,#3a2820 40%,#6a3a28)"></div>
  <div class="tile" role="img" aria-label="Cabinet wall" style="left:879px;top:370px;width:180px;height:120px;background:linear-gradient(160deg,#9a8a80,#3a2a24)"></div>
  <div class="tile" role="img" aria-label="Dining area with cabinets" style="left:879px;top:495px;width:180px;height:122px;background:linear-gradient(160deg,#cfc8be,#4a3830)"></div>
</section>

<section class="section services">
  <h2 class="title">SERVICES</h2>
  <div class="divider"></div>
  <div class="svc" style="left:314px">
    <h3>Residential</h3>
    <div class="photo" role="img" aria-label="Bedroom with dark built-in wardrobe" style="background:linear-gradient(160deg,#9c8e86,#3a2a24 55%,#8a7a70)"></div>
    <p>Here at Brindlemoor Custom Cabinets we are proud to be involved in the custom cabinet market. By employing and partnering up with local artisans we are able to deliver a product that is second to none.</p>
    <p>With our 3D Screen-to-Machine software you can see first hand exactly what you will be getting before a single piece is cut.</p>
  </div>
  <div class="svc" style="left:627px">
    <h3>Business</h3>
    <div class="photo" role="img" aria-label="Wall of white built-in shelving" style="background:linear-gradient(160deg,#6a7e88,#cfd4d6 50%,#3a4a52)"></div>
    <p>At Brindlemoor Custom Cabinets we understand that contractors, renovators, home builders, design firms and designers are the foundation of any cabinet shop. We believe that if we work with you to help your business succeed that, in turn, so will ours.</p>
    <p>We provide cabinets from design to completion however we also offer supply only cabinets built to your specifications.</p>
    <p>Work with a cabinet shop that wants your business!</p>
  </div>
</section>

<section class="section warranty">
  <h2 class="title">LIMITED WARRANTY</h2>
  <div class="terms">
    <p><b>Brindlemoor Custom Cabinets</b> warrants its products to the original consumer purchaser, to be free from defects in material and workmanship under normal residential use, for a period of two (2) years from the original date of purchase. This warranty is nontransferable. Hinges, Drawer Runners, and Mechanical Parts are covered under this warranty for two (2) years.</p>
    <p>During this warranty period, <b>Brindlemoor Custom Cabinets</b> will repair or replace, at our option, any cabinet or its component which proves to be defective in material and/or workmanship under normal installation, use and service. This warranty is limited to the replacement of defective parts and does not include improper storage, misuse or neglect.</p>
    <p>This warranty shall not apply to <b>Brindlemoor Custom Cabinet's</b> cabinetry or parts that have been subjected to alteration, modification, accident, abnormal use, extreme temperature, moisture levels, smoke, drawer slides, hinges, or plastic revolving shelves that have been exposed to excessive loads or abused, abrasive/citrus cleaning chemicals. Damages for naturally occurring events of nature such as fire, floods, or acts of God.</p>
    <p>This warranty does not apply to any products used or installed in conjunction with <b>Brindlemoor Custom Cabinets</b> such as plumbing fixtures, countertops (not provided and installed by Brindlemoor Custom Cabinets), or appliances, cabinetry or parts contrary to instructions furnished by <b>Brindlemoor Custom Cabinets</b> will void this warranty.</p>
    <p><strong>Special considerations:</strong><br>Finish deviations must be inspected by <b>Brindlemoor Custom Cabinets</b>. Determination will be made following the inspection whether to replace or return to the factory for refinishing or replacement.</p>
    <p>Stain variations: Since no two trees are the same, wood is a unique material with natural variations in grain, texture, and color. These variations may also cause considerable differences between samples and new cabinets. Please Note: Newly produced cabinets will never be the exact same color as aged cabinets.</p>
    <p>THE WARRANTY STATEMENTS CONTAINED IN THIS LIMITED WARRANTY SET FORTH THE ONLY EXPRESS WARRANTIES EXTENDED BY BRINDLEMOOR CUSTOM CABINETS FOR THE CABINETS, IN LIEU OF ALL OTHER WARRANTIES. THE PROVISIONS OF THE WARRANTY SHALL CONSTITUTE THE ENTIRE LIABILITY OF BRINDLEMOOR CUSTOM CABINETS AND THE PROPERTY OWNER'S EXCLUSIVE REMEDY FOR BREACH OF THE WARRANTY. BRINDLEMOOR CUSTOM CABINETS SHALL NOT BE LIABLE TO THE PROPERTY OWNER FOR INCIDENTAL OR CONSEQUENTIAL DAMAGES FOR BREACH OF AN EXPRESS OR IMPLIED WARRANTY ON THE CABINETS.<br>Some jurisdictions do not allow the exclusion or limitation of incidental or consequential damages, so the above limitations or exclusions may not apply to you. This warranty gives you specific rights and you may also have other rights which vary from jurisdiction to jurisdiction.</p>
  </div>
</section>

<section class="section contact">
  <h2 class="title">CONTACT</h2>
  <div class="form">
    <div class="field">Name</div>
    <div class="field">Email</div>
    <div class="field">Phone</div>
    <div class="field message">Message</div>
    <div class="submit">Submit</div>
  </div>
  <div class="details">
    <h4>Address:</h4>
    <div>4410 Range Road 190<br>Foxhill, Alberta<br>T0X 2B4</div>
    <hr>
    <div class="line"><span class="dot"><svg width="8" height="6" viewBox="0 0 8 6"><rect x=".5" y=".5" width="7" height="5" fill="none" stroke="#fff"/><path d="M.5 .5L4 3.5 7.5 .5" fill="none" stroke="#fff"/></svg></span>sales@brindlemoorcustomcabinets.com</div>
    <div class="line"><span class="dot"><svg width="8" height="8" viewBox="0 0 8 8"><path d="M1.5 .5l1.5 1.8-.8 1c.6 1.1 1.3 1.8 2.3 2.3l1-.8 1.8 1.5-1 1.2C3.8 7.3.7 4.2 .3 1.5z" fill="#fff"/></svg></span>555-318-4427 or 555-962-0375</div>
    <div class="social"><span></span><span></span><span></span></div>
  </div>
</section>

<footer class="section footer">©copyright 2016 All rights reserved</footer>

</body>
</html>
```